Industrial Inspection & Testing Company Needs Brochure

We need a brochure design for a company based in Western Pennsylvania, USA. Our company performs services mainly in industrial sites. These can include manufacturing, health & medical, power generation, and more. We use infrared thermography, vibration analysis, ultrasonic thickness testing, dynamic balancing and other practices to provide predictive maintenance to our customers. Please see our website for a more thorough explanation of our services. www.kortalinspect.com

Complete list of services:

Infrared Thermal Imaging
Vibration Analysis
High Temperature Video & Photography
High Speed Video
Laser Alignment
Dynamic Balancing
Motor Meggering
Leak Detection
Ultrasonic Thickness Testing
Oil Analysis

KRT, LLC - P.O. Box 4738 - Maple Hollow, PA 15842
Phone: 555-318-4471 / Fax: 555-318-4479

MISSION

KRT, LLC will provide the highest quality, cost effective, world class PdM services in the industry. Our commitment to continuing education and growth will afford our engineers the tools needed to stay on the cutting edge of technology. We believe in the implementation of Predictive Maintenance services to increase overall equipment reliability, reduce costs and improve profitability. Our goal is to provide continuous improvements to these processes. The company will network with various industry professionals to offer the widest range of equipment, training and reliability services available. Meeting these goals will ensure the company’s longevity and allow our valued customers to achieve the cost reduction goals that are needed in today’s competitive marketplace.
HISTORY
KRT, LLC was founded in March 1984, which emerged from the Granite Forge Industries’ Laboratory Campus, Monroeville, Pennsylvania. Its founders headed the Thermography and Photoinstrumentation Department of that facility.
While at the G. F. Industries Laboratory Campus, they established the utilization of thermography as a valuable tool for evaluating equipment and facilities in the steel industry. Their work set the standards for the use of thermography in the steel industry that continues today with KRT. Although the original thermographic equipment was crude, bulky and slow, KRT has maintained its position as an industry leader. Today KRT uses the most technologically advanced infrared systems available for on-site nondestructive industrial inspections.
In addition, while at G. F. Industries Laboratory, the founders of KRT pioneered the use of photographic cameras and high-speed motion pictures as another form of a predictive and preventative maintenance tool. Specially constructed camera systems with thermal protective housings were developed for inspecting blast furnace interior stockline armor areas, stove domes, and other high-temperature areas.
Today KRT remains on the cutting-edge in providing a wide range of nondestructive inspection services to industry.

***All of the photos and documents attached were either shot by us or purchased stock photos***

I realize that only a few images might be used, I just wanted to upload many to give designers a broad range to choose from.

Target Market(s)

Large industrial customers who use large amounts of electricity, heavy duty machinery, or both.

Industry/Entity Type

Industrial

Requirements
Must have
• Need a 3 full page tri-fold design (not skinny column tri-fold)

Contact information for our company, list of our services, our logo (possible redesign of logo), photos from our inspections that will be attached.
Nice to have
• List of services, breif explanation of each with graphical representation, contact information

```html
<!DOCTYPE html>
<html lang="en">
<head>
<meta charset="utf-8">
<title>KRT, LLC Tri-fold Brochure</title>
<link href="https://fonts.googleapis.com/css2?family=Open+Sans:wght@400;600;700&family=Roboto+Condensed:wght@700&display=swap" rel="stylesheet">
<style>
  :root {
    --page: #ffffff;
    --sheet: #f3f3f4;
    --sheet-edge: #d9d9dc;
    --ink: #3a3a3a;
    --navy: #1f2a78;
    --blue: #2a4fb0;
    --red: #c8202a;
    --purple: #3b1e8f;
    --panel: #e6e6e9;
  }
  * { box-sizing: border-box; margin: 0; padding: 0; }
  html, body { width: 834px; height: 1200px; overflow: hidden; background: var(--page); }
  body { font-family: "Open Sans", Arial, sans-serif; color: var(--ink); position: relative; }

  .sheet {
    position: absolute; left: 17px; width: 800px; height: 560px;
    background: linear-gradient(180deg, #fafafa, var(--sheet));
    border: 1px solid var(--sheet-edge);
  }
  .sheet--front { top: 20px; }
  .sheet--back { top: 620px; }

  .photo { position: absolute; border-radius: 12px; }

  /* front */
  .services { position: absolute; left: 18px; top: 213px; width: 240px; font-size: 9.5px; line-height: 12.4px; }
  .services h2 { font-size: 11px; font-weight: 600; color: var(--navy); margin-bottom: 2px; }
  .services h3 { font-size: 9.5px; font-weight: 400; color: var(--red); margin: 9px 0 1px 14px; }
  .services ul { list-style: none; }
  .services li::before { content: "\2022"; margin-right: 4px; }
  .services .sub li { margin-left: 14px; }

  .headline {
    position: absolute; left: 277px; top: 20px; width: 511px; height: 92px; border-radius: 14px;
    background: linear-gradient(90deg, #ffffff 0%, #ffffff 22%, #6b53c9 45%, var(--purple) 100%);
    font-family: "Roboto Condensed", Arial, sans-serif; color: #fff; text-align: right; padding: 12px 18px 0 0;
  }
  .headline .big { font-size: 23px; line-height: 24px; }
  .headline .small { font-size: 15.5px; margin-top: 4px; }
  .brand { position: absolute; left: 18px; top: 26px; display: flex; align-items: center; gap: 6px; }
  .brand .dot { width: 16px; height: 16px; border-radius: 50%; background: var(--purple); }
  .brand .name { font-family: "Open Sans", Arial, sans-serif; font-weight: 700; font-size: 30px; color: var(--purple); }

  .contact {
    position: absolute; left: 277px; top: 123px; width: 200px; height: 205px; border-radius: 14px;
    background: var(--panel); text-align: center; color: var(--navy); font-weight: 700; font-size: 11px; line-height: 13.5px; padding-top: 22px;
  }
  .contact .web { margin-top: 38px; }

  .logo-tile {
    position: absolute; left: 693px; top: 442px; width: 95px; height: 92px; border-radius: 12px;
    background: var(--panel); display: flex; align-items: center; justify-content: center; gap: 5px;
  }
  .logo-tile .dot { width: 12px; height: 12px; border-radius: 50%; background: var(--purple); }
  .logo-tile .name { font-weight: 700; font-size: 22px; color: var(--purple); }

  /* back */
  .block-title { position: absolute; font-size: 10.5px; font-weight: 600; color: var(--navy); }
  .body-text { position: absolute; font-size: 6.9px; line-height: 9.4px; text-align: justify; }
  .mission-text { left: 120px; top: 38px; width: 157px; }
  .history-text { left: 285px; top: 158px; width: 254px; font-size: 6.9px; line-height: 10.3px; }
  .back-web { position: absolute; left: 285px; top: 521px; width: 254px; text-align: center; font-weight: 700; font-size: 13px; color: var(--navy); }

  .service-list { position: absolute; left: 555px; top: 158px; width: 128px; font-size: 6.8px; line-height: 9.2px; }
  .service-list h3 { font-size: 7.2px; font-weight: 700; color: var(--red); margin: 8px 0 1px; }
  .service-list h3:first-child { margin-top: 0; }
  .service-list ul { list-style: none; padding-left: 4px; }
  .service-list li::before { content: "\2022"; margin-right: 3px; }
</style>
</head>
<body>

<section class="sheet sheet--front" aria-label="Brochure front">
  <div class="photo" role="img" aria-label="Photo of a transmission tower against blue sky" style="left:18px;top:77px;width:120px;height:123px;background:linear-gradient(160deg,#6fb0e6,#1f5aa8 60%,#1b2c55);"></div>
  <div class="photo" role="img" aria-label="Photo of a steel mill blast furnace" style="left:146px;top:69px;width:97px;height:139px;background:linear-gradient(180deg,#9aa2ad,#4b4d52 60%,#2a2a2c);"></div>

  <div class="services">
    <h2>services:</h2>
    <ul>
      <li>Infrared Thermal Imaging</li>
      <li>Vibration Analysis</li>
      <li>High Temperature Video &amp; Photography</li>
      <li>High Speed Video</li>
      <li>Laser Alignment</li>
      <li>Dynamic Balancing</li>
      <li>Motor Meggering</li>
      <li>Leak Detection</li>
      <li>Ultrasonic Thickness Testing</li>
      <li>Oil Analysis</li>
    </ul>
    <h3>Condition Monitoring &amp; PdM</h3>
    <ul class="sub">
      <li>Ultrasonic Thickness Testing</li>
      <li>Oil Analysis</li>
      <li>Infrared Thermal Imaging</li>
      <li>High Temperature Video &amp; Photography</li>
      <li>Vibration Analysis</li>
    </ul>
    <h3>Precision Maintenance</h3>
    <ul class="sub">
      <li>Laser Alignment</li>
      <li>Balancing</li>
      <li>Leak Detection</li>
      <li>Lubrication</li>
      <li>Training</li>
    </ul>
  </div>

  <header class="headline">
    <div class="brand"><span class="dot"></span><span class="name">KRT</span></div>
    <div class="big">HIGHEST QUALITY</div>
    <div class="big">COST EFFECTIVE</div>
    <div class="small">WORLD CLASS PDM SERVICES</div>
  </header>

  <address class="contact" style="font-style:normal;">
    <div>KRT, LLC</div>
    <div>P.O. Box 4738</div>
    <div>Maple Hollow, PA 15842</div>
    <div>Phone: 555-318-4471</div>
    <div>Fax: 555-318-4479</div>
    <div class="web">www.kortalinspect.com</div>
  </address>

  <div class="photo" role="img" aria-label="Photo of a power plant at dusk reflected in water" style="left:488px;top:123px;width:300px;height:205px;background:linear-gradient(180deg,#7d8fc4,#3d4f93 55%,#1a2350);"></div>
  <div class="photo" role="img" aria-label="Aerial photo of cooling towers with steam" style="left:277px;top:339px;width:200px;height:196px;background:linear-gradient(180deg,#c9cdd0,#8f9a84 55%,#5a6a4c);"></div>
  <div class="photo" role="img" aria-label="Photo of cooling towers under blue sky" style="left:488px;top:339px;width:194px;height:92px;background:linear-gradient(180deg,#3f7fd0,#8fb5e0 60%,#a9a89a);"></div>
  <div class="photo" role="img" aria-label="Photo of industrial equipment" style="left:693px;top:339px;width:95px;height:92px;background:linear-gradient(160deg,#b98a6a,#6a4a3a);"></div>
  <div class="photo" role="img" aria-label="Photo of a power station under blue sky" style="left:488px;top:442px;width:94px;height:92px;background:linear-gradient(180deg,#4d8ad8,#a4b9cf 60%,#6c6f70);"></div>
  <div class="photo" role="img" aria-label="Photo of a water treatment plant" style="left:590px;top:442px;width:92px;height:92px;background:linear-gradient(180deg,#3a78cf,#86a7c9 55%,#5e6a73);"></div>
  <div class="logo-tile"><span class="dot"></span><span class="name">KRT</span></div>
</section>

<section class="sheet sheet--back" aria-label="Brochure back">
  <div class="photo" role="img" aria-label="Photo of glowing molten steel" style="left:12px;top:12px;width:99px;height:88px;background:linear-gradient(160deg,#f0a040,#c0401c 55%,#3a1a14);"></div>
  <div class="photo" role="img" aria-label="Photo of oil pumpjacks at sunset" style="left:12px;top:115px;width:99px;height:89px;background:linear-gradient(180deg,#f6c24a,#e07a1e 60%,#4a2a10);"></div>
  <div class="photo" role="img" aria-label="Infrared thermal image of equipment" style="left:12px;top:216px;width:99px;height:92px;background:linear-gradient(150deg,#f2e24a,#e0308a 45%,#4a1a9a);"></div>
  <div class="photo" role="img" aria-label="Photo of electrical substation" style="left:12px;top:346px;width:265px;height:193px;background:linear-gradient(180deg,#e2e4e6,#a7adb3 55%,#6a7076);"></div>

  <h2 class="block-title" style="left:126px;top:16px;">Our Mission</h2>
  <p class="body-text mission-text">KRT, LLC will provide the highest quality, cost effective, world class PdM services in the industry. Our commitment to continuing education and growth will afford our engineers the tools needed to stay on the cutting edge of technology. We believe in the implementation of Predictive Maintenance services to increase overall equipment reliability, reduce costs and improve profitability. Our goal is to provide continuous improvements to these processes. The company will network with various industry professionals to offer the widest range of equipment, training and reliability services available. Meeting these goals will ensure the company’s longevity and allow our valued customers to achieve the cost reduction goals that are needed in today’s competitive marketplace.</p>

  <div class="photo" role="img" aria-label="Photo of cooling towers at dusk" style="left:285px;top:12px;width:251px;height:114px;background:linear-gradient(180deg,#1c2a55,#5a5f8a 50%,#c88a3a);"></div>
  <h2 class="block-title" style="left:287px;top:134px;">History</h2>
  <p class="body-text history-text">KRT, LLC will provide the highest quality, cost effective, world class PdM services in the industry. Our commitment to continuing education and growth will afford our engineers the tools needed to stay on the cutting edge of technology. We believe in the implementation of Predictive Maintenance services to increase overall equipment reliability, reduce costs and improve profitability. Our goal is to provide continuous improvements to these processes. The company will network with various industry professionals to offer the widest range of equipment, training and reliability services available. Meeting these goals will ensure the company’s longevity and allow our valued customers to achieve the cost reduction goals that are needed in today’s competitive marketplace. KRT, LLC was founded in March 1984, which emerged from the Granite Forge Industries’ Laboratory Campus, Monroeville, Pennsylvania. Its founders headed the Thermography and Photoinstrumentation Department of that facility. While at the G. F. Industries Laboratory Campus, they established the utilization of thermography as a valuable tool for evaluating equipment and facilities in the steel industry. Their work set the standards for the use of thermography in the steel industry that continues today with KRT. Although the original thermographic equipment was crude, bulky and slow, KRT has maintained its position as an industry leader. Today KRT uses the most technologically advanced infrared systems available for on-site nondestructive industrial inspections. In addition, while at G. F. Industries Laboratory, the founders of KRT pioneered the use of photographic cameras and high-speed motion pictures as another form of a predictive and preventative maintenance tool. Specially constructed camera systems with thermal protective housings were developed for inspecting blast furnace interior stockline armor areas, stove domes, and other high-temperature areas. Today KRT remains on the cutting-edge in providing a wide range of nondestructive inspection services to industry.</p>
  <div class="back-web">www.kortalinspect.com</div>

  <div class="photo" role="img" aria-label="Close-up photo of large industrial gears" style="left:551px;top:12px;width:231px;height:111px;background:linear-gradient(160deg,#9a9a9a,#555 55%,#2a2a2a);"></div>
  <h2 class="block-title" style="left:555px;top:134px;">Our Services</h2>
  <div class="service-list">
    <h3>Thermography</h3>
    <ul><li>Thermographic Tour</li><li>Building Inspections</li><li>Electrical Inspections</li><li>Roof Inspections</li><li>Infrared Thermal Imaging</li></ul>
    <h3>Condition Monitoring &amp; Pdm</h3>
    <ul><li>Vibration Analysis</li><li>Oil Analysis</li><li>Ultrasonic Leak Detection</li><li>Ultrasonic Thickness Testing</li></ul>
    <h3>Precision Maintenance</h3>
    <ul><li>Precision Laser Alignment</li><li>Balancing</li></ul>
    <h3>Video Inspection</h3>
    <ul><li>Specialty Video</li><li>High Temp Video Inspections</li><li>Slow Motion Study</li></ul>
  </div>
  <div class="photo" role="img" aria-label="Photo of a refinery structure against blue sky" style="left:685px;top:139px;width:97px;height:92px;background:linear-gradient(180deg,#4a86d0,#9a8a6a 65%,#5a4a3a);"></div>
  <div class="photo" role="img" aria-label="Photo of industrial piping and machinery" style="left:685px;top:242px;width:97px;height:112px;background:linear-gradient(180deg,#7a9ac0,#8a6a4a 60%,#3a2a20);"></div>
  <div class="photo" role="img" aria-label="Photo of a refinery lit at sunset" style="left:551px;top:408px;width:231px;height:116px;background:linear-gradient(180deg,#3a4a8a,#c0607a 45%,#f09a40 65%,#2a1a20);"></div>
</section>

</body>
</html>
```